KVO Brochure Design Project

We need a 4 page brochure (A4 size) prepared to announce a new consulting service. The consulting service is highly professional and is aimed at business owners of small to medium businesses and their accountants.
Updates

Thankyou for the designs posted so far, please see a new file uploaded that has hi-res diagrams for the brochure, regards

please use the hi res graphics I uploaded today, thanks

Thankyou for your designs please: 1) put the title on the front page ie "A unique Offering to Business Owners" should be on the first page 2) please upload all 4 pages so that I can see that the text fits well across 4 pages 3) please use the hi res graphics in the file uploaded yesterday.

Thanks again!

Designers - please note the original brief: it must fit on a brochure 4 x A4 pages (ie A3 folded brochure)

Target Market(s)

business owners of companies worth $3M to $30M + accountants, lawyers and other professionals

Industry/Entity Type

Business

Requirements
Must have
• Must appear professional - not gimicky

```html
<!DOCTYPE html>
<html lang="en">
<head>
<meta charset="utf-8">
<title>Brochure – Divestment Readiness Assessment</title>
<link href="https://fonts.googleapis.com/css2?family=Oswald:wght@400;500&family=Open+Sans:wght@400;600&family=PT+Sans+Narrow:wght@400;700&family=Titillium+Web:wght@400;600&display=swap" rel="stylesheet">
<style>
  :root {
    --ink: #14191f;
    --charcoal: #474a4e;
    --slate-light: #8a9ab0;
    --slate: #3b4b62;
    --gold: #d49b2a;
    --gold-deep: #c8952c;
    --paper: #dedede;
    --paper-light: #e8e8e8;
    --grey-block: #b9b9b9;
    --white: #ffffff;
    --stage: #f3f3f3;
    --text-dark: #2b2b2b;
    --brand-yellow: #e2cf2f;
  }
  * { box-sizing: border-box; margin: 0; padding: 0; }
  html, body { width: 1200px; height: 1000px; overflow: hidden; background: var(--stage); }
  .canvas { position: relative; width: 1200px; height: 1000px; overflow: hidden; }

  .page { position: absolute; width: 360px; height: 509px; overflow: hidden; box-shadow: 0 2px 8px rgba(0,0,0,.18); }

  /* ---------- Cover ---------- */
  .cover { left: 28px; top: 245px; background: var(--ink); }
  .cover-top-left { position: absolute; left: 0; top: 0; width: 180px; height: 172px; background: var(--charcoal); }
  .cover-top-right { position: absolute; left: 180px; top: 0; width: 180px; height: 172px; background: var(--slate-light); }
  .brand-box { position: absolute; left: 108px; top: 30px; width: 144px; height: 90px; background: var(--ink); border: 3px solid var(--white); display: flex; align-items: center; justify-content: center; gap: 6px; }
  .brand-dot { width: 9px; height: 9px; border-radius: 50%; background: var(--brand-yellow); }
  .brand-name { font-family: "Open Sans", sans-serif; font-weight: 600; font-size: 10px; color: var(--brand-yellow); letter-spacing: .02em; }
  .cover-tagline { position: absolute; left: 0; top: 136px; width: 360px; text-align: center; font-family: "Oswald", sans-serif; font-weight: 500; font-size: 13.5px; letter-spacing: .06em; color: var(--white); }
  .cover-photo { position: absolute; left: 0; top: 172px; width: 360px; height: 160px; background: linear-gradient(180deg, #4d5f7c 0%, #9fb3cc 35%, #2f3744 62%, #c99a34 82%, #6f5a2b 100%); }
  .cover-gold { position: absolute; left: 0; top: 345px; width: 125px; height: 164px; background: var(--gold-deep); }
  .cover-dark { position: absolute; left: 125px; top: 318px; width: 235px; height: 191px; background: var(--ink); }
  .cover-question { position: absolute; left: 140px; top: 334px; width: 212px; font-family: "Oswald", sans-serif; font-weight: 500; font-size: 14px; line-height: 1.45; letter-spacing: .09em; color: var(--white); text-align: center; }
  .cover-stat { position: absolute; left: 146px; top: 398px; width: 200px; font-family: "Open Sans", sans-serif; font-weight: 600; font-size: 12.5px; line-height: 1.5; color: var(--gold); text-align: right; }

  /* ---------- Spread ---------- */
  .spread-left { left: 416px; top: 245px; background: var(--white); }
  .spread-right { left: 778px; top: 245px; background: var(--white); }

  .col { position: absolute; top: 0; bottom: 0; overflow: hidden; }
  .body-copy { font-family: "PT Sans Narrow", sans-serif; font-size: 6px; line-height: 1.42; }
  .body-copy p { margin-bottom: 4px; }
  .body-copy .lead { font-weight: 700; }
  .body-copy ol, .body-copy ul { margin: 0 0 4px 0; padding-left: 8px; }
  .body-copy li { margin-bottom: 3px; }
  .body-copy ol.sub { list-style: lower-alpha; padding-left: 10px; margin-top: 2px; }
  .body-copy ul { list-style: disc; }
  .section-head { position: absolute; left: 0; right: 0; padding: 0 10px; display: flex; align-items: center; font-family: "Titillium Web", sans-serif; font-weight: 400; font-size: 11px; line-height: 1.2; color: var(--white); }

  /* left page */
  .col-why { left: 0; width: 135px; background: var(--paper); }
  .col-why .section-head { top: 14px; height: 52px; background: var(--ink); }
  .col-why .body-copy { position: absolute; left: 8px; right: 8px; top: 76px; height: 312px; overflow: hidden; color: var(--text-dark); }
  .photo-money { position: absolute; left: 0; top: 392px; width: 135px; height: 90px; background: linear-gradient(135deg, #6a5530 0%, #b89a5c 45%, #d8c9a0 70%, #5a4a2c 100%); }
  .col-why .strip { position: absolute; left: 0; bottom: 0; width: 135px; height: 27px; background: var(--slate); }

  .col-what { left: 135px; width: 225px; background: var(--gold); }
  .col-what .top { position: absolute; left: 0; top: 0; width: 225px; height: 52px; background: var(--paper-light); }
  .col-what .section-head { top: 52px; height: 54px; background: var(--slate); }
  .col-what .body-copy { position: absolute; left: 9px; right: 9px; top: 112px; height: 362px; overflow: hidden; color: var(--ink); }
  .col-what .strip { position: absolute; left: 0; bottom: 0; width: 225px; height: 27px; background: var(--slate); }

  /* right page */
  .col-benefits { left: 0; width: 195px; background: var(--slate); }
  .col-benefits .top { position: absolute; left: 0; top: 0; width: 195px; height: 22px; background: var(--white); }
  .col-benefits .section-head { top: 22px; height: 36px; background: var(--ink); }
  .col-benefits .body-copy { position: absolute; left: 10px; right: 10px; top: 66px; height: 345px; overflow: hidden; color: var(--white); }
  .col-benefits .body-copy ol { list-style: none; padding-left: 0; }
  .col-benefits .body-copy li { margin-bottom: 10px; }
  .photo-pencils { position: absolute; left: 20px; top: 418px; width: 112px; height: 58px; background: linear-gradient(120deg, #f4f1ea 0%, #d9a35a 40%, #8a6a45 70%, #efe9df 100%); }
  .col-benefits .base { position: absolute; left: 0; bottom: 0; width: 195px; height: 24px; background: var(--paper-light); }

  .col-process { left: 195px; width: 165px; background: var(--paper-light); }
  .col-process .top { position: absolute; left: 0; top: 0; width: 165px; height: 22px; background: var(--grey-block); }
  .col-process .section-head { top: 22px; height: 54px; background: var(--gold); color: var(--ink); font-size: 11.5px; }
  .col-process .body-copy { position: absolute; left: 9px; right: 8px; top: 84px; bottom: 10px; overflow: hidden; color: var(--text-dark); font-size: 5.8px; }
  .col-process .body-copy ol { list-style: none; padding-left: 0; }
  .col-process .body-copy li { margin-bottom: 4px; }
  .num { font-weight: 700; }
</style>
</head>
<body>
<main class="canvas">

  <!-- Front cover -->
  <section class="page cover" aria-label="Front cover">
    <div class="cover-top-left"></div>
    <div class="cover-top-right"></div>
    <div class="brand-box">
      <span class="brand-dot"></span>
      <span class="brand-name">Harbourline Capital</span>
    </div>
    <h1 class="cover-tagline">A UNIQUE OFFERING TO BUSINESS OWNERS</h1>
    <div class="cover-photo" role="img" aria-label="Photograph of a modern glass boardroom with a polished gold-lit floor"></div>
    <div class="cover-gold"></div>
    <div class="cover-dark"></div>
    <h2 class="cover-question">WHY CONDUCT A DIVESTMENT READINESS ASSESSMENT?</h2>
    <p class="cover-stat">70% of owners of small and medium businesses will seek to exit their business over the next 10 years.</p>
  </section>

  <!-- Inside spread: left page -->
  <section class="page spread-left" aria-label="Inside left page">
    <div class="col col-why">
      <h2 class="section-head">Why conduct a divestment readiness assessment?</h2>
      <div class="body-copy">
        <p class="lead">70% of owners of small and medium businesses will seek to exit their business over the next 10 years.</p>
        <p>Approximately 60% of Australian businesses are owned by baby boomers, who tend to have most of their wealth locked in their business. As baby boomers enter their 60s and 70s over the coming decade most will need to exit their businesses to unlock funds for retirement.</p>
        <p>As a result, more than two-thirds of all Australian SMEs will seek to exit within a single decade, flooding the market with businesses for sale – creating what is being referred to as the “Baby Boomer Tsunami”.</p>
        <p>With so many businesses for sale on the market, many owners will be unable to exit – or sell for fair value, leaving them with significantly reduced funds for retirement.</p>
        <p>To unlock the maximum value within what is in most cases, their largest asset, owners must ensure their businesses are exceptionally well prepared and ready for sale. Given that 75% of business owners have</p>
      </div>
      <div class="photo-money" role="img" aria-label="Photograph of banknotes with a dollar sign"></div>
      <div class="strip"></div>
    </div>

    <div class="col col-what">
      <div class="top"></div>
      <h2 class="section-head">What is a divestment readiness assessment?</h2>
      <div class="body-copy">
        <p class="lead">The Divestment Readiness Assessment provides an independent assessment of the readiness of a business for sale and where appropriate, identifies the specific initiatives that would optimise the sale outcome for the business owner.</p>
        <p>The assessment is conducted by consulting professionals and is supported by M&amp;A Specialists. It provides the business owner with the following:</p>
        <ol>
          <li>The overall preparedness of their business for sale in the short-term. This considers 2 dimensions:
            <ol class="sub">
              <li>The relative ease with which the business can be sold based on its current structure in the current market; and</li>
              <li>The relative financial performance of the business compared with its potential.</li>
            </ol>
          </li>
          <li>An appraisal that provides the assessed value range of the business in its current state if presented to market in the short-term. The appraisal considers the attractiveness of the business to a variety of buyers such as financial investors and industry acquirers.</li>
          <li>The high priority initiatives that would make the business more saleable and/or substantially improve the anticipated sale price of the business.
            <p>The Divestment Readiness Assessment is focused on identifying those initiatives that will substantially enhance the sale outcome.</p>
          </li>
          <li>An example of their business’ investment highlights as would be presented to the market if they wish to progress to a sale.</li>
        </ol>
        <p>Additionally, if the client has an interest in understanding more of the process that would be applied to sell their business, the consultant will facilitate a session with an M&amp;A Specialist which will include:</p>
        <ul>
          <li>An overview of the sale process</li>
          <li>Indicative target acquirers for the client’s business</li>
          <li>Marketing approach and channels that are applicable to the client’s business</li>
          <li>Responses to frequently asked questions such as “how does the M&amp;A Specialist maintain the confidentiality of a business during the sale process?”</li>
        </ul>
      </div>
      <div class="strip"></div>
    </div>
  </section>

  <!-- Inside spread: right page -->
  <section class="page spread-right" aria-label="Inside right page">
    <div class="col col-benefits">
      <div class="top"></div>
      <h2 class="section-head">Benefits to the client</h2>
      <div class="body-copy">
        <p class="lead">The Divestment Readiness Assessment is intended to be an ideal interim phase for any client that wishes to assess and/or optimise their business for sale – whether or not they intend to sell in the short-term.</p>
        <p>The Divestment Readiness Assessment is a consulting engagement designed to provide a client with independent advice regarding their exit options and the readiness of their business for sale. At no stage during the Divestment Readiness Assessment is there an expectation that a client will proceed to a sale.</p>
        <p>The Divestment Readiness Assessment is designed to deliver the following benefits to a client:</p>
        <ol>
          <li><span class="num">1.</span> Provide independent advice that is in the best interests of the client</li>
          <li><span class="num">2.</span> Greatly assist the client to decide whether they should proceed with a sale in the short-term</li>
          <li><span class="num">3.</span> Identify specific actions that are expected to substantially improve the client’s sale outcome</li>
          <li><span class="num">4.</span> Enable the client to understand the likely value they will achieve at exit</li>
          <li><span class="num">5.</span> Provide the client with an understanding of the sale process</li>
          <li><span class="num">6.</span> Serve as a “stepping-stone” for client who wish to consider selling in the future</li>
          <li><span class="num">7.</span> Capture key information that would “kick-start” the client’s Information Memorandum and disclosure documentation should the client wish to proceed to sale</li>
        </ol>
      </div>
      <div class="photo-pencils" role="img" aria-label="Photograph of a cup of sharpened pencils"></div>
      <div class="base"></div>
    </div>

    <div class="col col-process">
      <div class="top"></div>
      <h2 class="section-head">Divestment readiness assessment process</h2>
      <div class="body-copy">
        <p class="lead">Unlike generalist consulting reviews, the Divestment Readiness Assessment is a specialist activity focused on assessing and optimising the potential business sale outcome</p>
        <p>The Divestment Readiness Assessment is conducted as follows:</p>
        <ol>
          <li><span class="num">1.</span> Introduction: the consultant provides an overview of the assessment process and outlines key information that is required to support the Review</li>
          <li><span class="num">2.</span> Onsite review: the consultant will meet the client and tour the client’s business if applicable. The consultant will work through the review with the client (typically half a day to a full day)</li>
          <li><span class="num">3.</span> Analysis: the consultant will work with the M&amp;A Specialist to analyse the information, assess the readiness of the business for sale and to complete the current market value range of the business.</li>
          <li><span class="num">4.</span> Sale Optimisation Recommendations: the consultant will work with the M&amp;A Specialist to determine whether there are any high priority initiatives that would likely substantially improve the sale outcome for the client.</li>
          <li><span class="num">5.</span> Presentation of outcomes: the consultant will then meet with the client to present the outcomes of the Divestment Readiness Assessment. The consultant will provide the client with the complete Divestment Readiness Report at that meeting and will schedule a follow-up meeting. The presentation will typically take 2 hours.</li>
          <li><span class="num">6.</span> Follow-up: typically within 2–4 weeks of presenting the Divestment Readiness Report, the consultant will meet with the client to answer any specific questions and to discuss next steps (if applicable).</li>
          <li><span class="num">7.</span> Optional session with the M&amp;A Specialist: should the client wish to learn more of the M&amp;A process, the consultant will facilitate a session with the M&amp;A Specialist to provide an overview of the sales process and to respond to any questions the client may have.</li>
          <li><span class="num">8.</span> Optional implementation support: should the client have an interest in gaining assistance to implement some or all of the recommendations, the consultant will develop a proposal tailored to the client’s needs.</li>
        </ol>
      </div>
    </div>
  </section>

</main>
</body>
</html>
```